I am a general contractor in Portland, Or. I would like a clean and simple design layout, maybe using the "didot" font, blue and dark bronze in colors are preferred. On one side of the card, it would be nice to have a logo(attached photo) and business name(KBT Construction). I don't need my job title on the card, just some thing along the lines of "harold pike, general contractor". Thanks much.

Target Market(s)

Adults from 30-55 years old. Middle to upper class.

Industry/Entity Type

Contractor

Contact Information for Business Card

KBT Construction
Harold M. Pike
2943 NE 71st Ave.
Portland, Or. 97288
503.627.9184

Font styles to use
Other font styles liked:
• didot

Colors
3277b5
7f7f7f

Requirements
Should not have
• Too much going on.

```html
<!DOCTYPE html>
<html lang="en">
<head>
<meta charset="utf-8">
<title>KBT Construction – Business Card</title>
<link href="https://fonts.googleapis.com/css2?family=Arimo:ital,wght@0,400;0,700&family=GFS+Didot&display=swap" rel="stylesheet">
<style>
  :root {
    --brand-blue: #1a68a8;
    --brand-grey: #7f7f7f;
    --name-grey: #6e6e6e;
    --card-white: #f4f4f4;
    --backdrop: #e4e4e4;
    --text-on-blue: #ffffff;
  }
  * { margin: 0; padding: 0; box-sizing: border-box; }
  html, body {
    width: 1200px;
    height: 1200px;
    overflow: hidden;
    background: var(--backdrop);
  }
  .sheet {
    position: relative;
    width: 1200px;
    height: 1200px;
    display: flex;
    flex-direction: column;
    align-items: center;
    justify-content: center;
    gap: 100px;
  }
  .card {
    position: relative;
    width: 700px;
    height: 400px;
    background: var(--card-white);
    overflow: hidden;
    box-shadow: 0 6px 18px rgba(0,0,0,0.12);
  }

  /* Contact side */
  .contact-band {
    position: absolute;
    left: 0; right: 0; bottom: 0;
    height: 220px;
    background: var(--brand-blue);
  }
  .brand-mark {
    position: absolute;
    display: flex;
    align-items: center;
    gap: 10px;
    font-family: "Arimo", Arial, sans-serif;
    font-weight: 700;
    color: var(--brand-blue);
    text-transform: uppercase;
    letter-spacing: 0.04em;
  }
  .brand-mark .dot {
    border-radius: 50%;
    background: var(--brand-blue);
    flex: none;
  }
  .card--contact .brand-mark {
    left: 40px;
    top: 78px;
    font-size: 15px;
  }
  .card--contact .brand-mark .dot { width: 14px; height: 14px; }
  .person {
    position: absolute;
    left: 250px;
    top: 86px;
  }
  .person__name {
    font-family: "Arimo", Arial, sans-serif;
    font-weight: 700;
    font-size: 32px;
    color: var(--name-grey);
    line-height: 1;
  }
  .person__role {
    font-family: "GFS Didot", "Didot", serif;
    font-size: 18px;
    color: var(--brand-blue);
    margin-top: 6px;
    padding-left: 28px;
  }
  .address {
    position: absolute;
    left: 268px;
    top: 200px;
    font-family: "Arimo", Arial, sans-serif;
    font-size: 24px;
    line-height: 1.25;
    color: var(--text-on-blue);
  }

  /* Brand side */
  .card--brand .brand-mark {
    left: 0; right: 0;
    top: 150px;
    justify-content: center;
    font-size: 36px;
  }
  .card--brand .brand-mark .dot { width: 28px; height: 28px; }
  .accent-line {
    position: absolute;
    left: 0; right: 0;
    bottom: 64px;
    height: 9px;
    background: var(--brand-blue);
  }
  .grey-band {
    position: absolute;
    left: 0; right: 0; bottom: 0;
    height: 64px;
    background: var(--brand-grey);
  }
</style>
</head>
<body>
  <main class="sheet">
    <section class="card card--contact" aria-label="Business card, contact side">
      <div class="contact-band"></div>
      <div class="brand-mark"><span class="dot"></span>KBT Construction</div>
      <div class="person">
        <p class="person__name">Harold M. Pike</p>
        <p class="person__role">general contractor</p>
      </div>
      <address class="address" style="font-style: normal;">
        2943 NE 71st Ave. Portland<br>
        97288 503.627.9184
      </address>
    </section>

    <section class="card card--brand" aria-label="Business card, brand side">
      <div class="brand-mark"><span class="dot"></span>KBT Construction</div>
      <div class="accent-line"></div>
      <div class="grey-band"></div>
    </section>
  </main>
</body>
</html>
```